BEREAN FELLOWSHIP GLOBAL.

THIS IS A PRAISE AND WORSHIP MEETING, WORTH NOTING, THAT ITS OUR FIRST MEETING. OUR THEME AND VISION......" Creating a platform for Interaction between Man and God". This should stand out. We also have a logo and I will email it to the designer that takes the job. We will have three pictures on the flier. Red is favourite color........ DATE OF THE MEETING. Saturday NOV 11th 2017. 6:30pm-9pm. Venue STILLWATER HARVEST CHAPEL 48260 Juniper Crest Ave, Auburn Wa 98347. Punch line at the bottom.....' the PRAISE to be'

Target Market(s)

Youth and adults.

Industry/Entity Type

Performing Art

Font styles to use
Decorative

Colors

Designer to choose colors to be used in the design.

Requirements
Must have
• The first design of the attached Logo. And the words......CREATING A PLATFORM FOR INTERACTION BETWEEN MAN AND GOD.
Should not have
• Pictures of three individuals. I have one but waiting for 2. I can send them later. The picture that is attached is of Samuel T Odhiambo.

```html
<!DOCTYPE html>
<html lang="en">
<head>
<meta charset="utf-8">
<title>Berean Fellowship Global – Praise and Worship Meeting</title>
<link href="https://fonts.googleapis.com/css2?family=Oswald:wght@500;600&family=Tinos:wght@400;700&family=Open+Sans:wght@400;700&display=swap" rel="stylesheet">
<style>
  :root{
    --red:#c0161a;
    --deep-red:#8a0f0c;
    --gold:#f2c14e;
    --gold-light:#fbe28f;
    --ink:#1c1c1c;
    --black:#0d0b0a;
    --white:#ffffff;
    --grey-line:#8d8d8d;
  }
  *{box-sizing:border-box;margin:0;padding:0}
  html,body{width:1041px;height:1200px;overflow:hidden;background:var(--white)}
  .flyer{position:relative;width:1041px;height:1200px;overflow:hidden;background:var(--white)}

  /* Header scene */
  .hero{position:absolute;left:0;top:0;width:1041px;height:505px;
    background:linear-gradient(180deg,#f6c35a 0%,#e5a243 35%,#b8652a 62%,#8c1d10 82%,var(--deep-red) 100%)}
  .hero-scene{position:absolute;inset:0}
  .speakers{position:absolute;left:0;top:0;width:1041px;height:505px}
  .speaker-photo{position:absolute;width:232px;height:232px;border-radius:50%;
    border:7px solid var(--red);background:radial-gradient(circle at 50% 40%,#8a8680 0%,#4a4541 55%,#1d1a18 100%)}
  .speaker-photo.one{left:186px;top:168px}
  .speaker-photo.two{left:396px;top:162px;background:radial-gradient(circle at 50% 40%,#6f7d9a 0%,#3b4660 55%,#1a1e2a 100%)}
  .speaker-photo.three{left:612px;top:168px}
  .name-banner{position:absolute;left:0;top:0}
  .speaker-names{position:absolute;top:412px;left:0;width:1041px;height:70px}
  .speaker-name{position:absolute;width:200px;text-align:center;font-family:'Oswald',sans-serif;
    font-weight:500;font-size:20px;line-height:28px;color:#2b1a0a;letter-spacing:.3px}
  .speaker-name.one{left:201px}
  .speaker-name.two{left:411px}
  .speaker-name.three{left:628px}
  .hero-rule{position:absolute;left:0;top:500px;width:1041px;height:5px;background:var(--grey-line)}

  /* Theme section */
  .theme{position:absolute;left:0;top:505px;width:1041px;height:310px;background:var(--white)}
  .brand{position:absolute;left:0;top:34px;width:1041px;text-align:center}
  .brand-name{font-family:'Tinos',serif;font-weight:400;font-size:32px;line-height:34px;color:var(--ink);letter-spacing:.8px}
  .headline{position:absolute;left:0;top:128px;width:1041px;text-align:center;font-family:'Tinos',serif;font-weight:700;color:var(--ink)}
  .headline-top{display:block;font-size:50px;line-height:56px;letter-spacing:.5px}
  .headline-mid{display:flex;align-items:center;justify-content:center;gap:14px;font-size:27px;line-height:34px;letter-spacing:1px;margin-top:2px}
  .headline-mid::before,.headline-mid::after{content:"";display:block;width:160px;height:3px;background:var(--red)}
  .headline-main{display:block;font-size:90px;line-height:92px;letter-spacing:-1px;margin-top:2px}
  .headline-main .accent{color:var(--red)}

  /* Details section */
  .details{position:absolute;left:0;top:815px;width:1041px;height:385px;
    background:radial-gradient(ellipse at 50% 10%,#3a2a12 0%,#1a130b 35%,var(--black) 70%)}
  .info-box{position:absolute;text-align:center}
  .info-box.date,.info-box.time{top:30px;height:206px;width:238px;background:var(--red);color:var(--white)}
  .info-box.date{left:156px}
  .info-box.time{left:642px}
  .info-box.venue{left:396px;top:20px;width:244px;height:226px;background:var(--white);color:var(--ink)}
  .info-label{display:block;margin:18px auto 0;width:182px;height:38px;background:#1e1e1e;color:var(--white);
    font-family:'Oswald',sans-serif;font-weight:500;font-size:30px;line-height:38px}
  .venue .info-label{margin-top:20px;width:198px}
  .date-value{font-family:'Oswald',sans-serif;font-weight:600;font-size:34px;line-height:38px;margin-top:8px}
  .date-year{display:block;font-size:54px;line-height:58px}
  .time-value{font-family:'Oswald',sans-serif;font-weight:600;font-size:44px;line-height:50px;margin-top:14px}
  .time-value .small{font-size:32px}
  .pin{display:block;margin:12px auto 4px}
  .venue-text{font-family:'Oswald',sans-serif;font-weight:500;font-size:19px;line-height:22px;text-transform:uppercase}
  .contact{position:absolute;left:0;top:262px;width:1041px;height:44px;line-height:44px;text-align:center;color:var(--white);font-family:'Open Sans',sans-serif}
  .contact-label{font-size:25px}
  .contact-numbers{font-size:32px;margin-left:6px}
  .punchline{position:absolute;left:0;top:318px;width:1041px;height:45px;background:var(--red);color:var(--white);
    text-align:center;font-family:'Open Sans',sans-serif;font-size:29px;line-height:45px;letter-spacing:5px}
  .punchline strong{font-weight:700}
</style>
</head>
<body>
<main class="flyer">
  <section class="hero">
    <div class="hero-scene" role="img" aria-label="Golden sunrise over misty mountains with a person standing on a peak, arms outstretched"></div>
    <svg class="name-banner" width="1041" height="505" viewBox="0 0 1041 505" aria-hidden="true">
      <defs>
        <linearGradient id="bannerGold" x1="0" y1="0" x2="1" y2="1">
          <stop offset="0" stop-color="#d9a63a"/>
          <stop offset=".45" stop-color="#fbe28f"/>
          <stop offset="1" stop-color="#e0a93c"/>
        </linearGradient>
      </defs>
      <polygon points="73,352 942,352 890,480 125,480" fill="url(#bannerGold)"/>
    </svg>
    <div class="speakers">
      <div class="speaker-photo one" role="img" aria-label="Portrait photo of Leon Varga"></div>
      <div class="speaker-photo three" role="img" aria-label="Portrait photo of Pastor Dennis Holloway"></div>
      <div class="speaker-photo two" role="img" aria-label="Portrait photo of Samuel T Odhiambo"></div>
    </div>
    <div class="speaker-names">
      <p class="speaker-name one">LEON<br>VARGA</p>
      <p class="speaker-name two">SAMUEL<br>T ODHIAMBO</p>
      <p class="speaker-name three">PASTOR<br>DENNIS HOLLOWAY</p>
    </div>
    <div class="hero-rule"></div>
  </section>

  <section class="theme">
    <div class="brand">
      <p class="brand-name">BEREAN FELLOWSHIP<br>GLOBAL</p>
    </div>
    <h1 class="headline">
      <span class="headline-top">CREATING A PLATFORM FOR</span>
      <span class="headline-mid">INTERACTION BETWEEN</span>
      <span class="headline-main"><span class="accent">MAN</span> AND <span class="accent">GOD</span></span>
    </h1>
  </section>

  <section class="details">
    <div class="info-box date">
      <span class="info-label">DATE</span>
      <p class="date-value">SATURDAY<br>NOV 11TH<span class="date-year">2017</span></p>
    </div>
    <div class="info-box venue">
      <span class="info-label">VENUE</span>
      <svg class="pin" width="22" height="26" viewBox="0 0 22 26" aria-hidden="true">
        <path d="M11 24 C5 16 3 12 3 9 A8 8 0 0 1 19 9 C19 12 17 16 11 24 Z" fill="none" stroke="#333" stroke-width="1.6"/>
        <circle cx="11" cy="9" r="3" fill="none" stroke="#333" stroke-width="1.6"/>
        <line x1="4" y1="25" x2="18" y2="25" stroke="#333" stroke-width="1.4"/>
      </svg>
      <p class="venue-text">Stillwater Harvest<br>Chapel<br>48260 Juniper Crest Ave,<br>Auburn WA 98347</p>
    </div>
    <div class="info-box time">
      <span class="info-label">TIME</span>
      <p class="time-value">6:30PM<br><span class="small">TO</span> 9PM</p>
    </div>
    <p class="contact"><span class="contact-label">Further Info, Call:</span><span class="contact-numbers">0551203867 / 0552718340</span></p>
    <p class="punchline">THE <strong>PRAISE</strong> TO BE</p>
  </section>
</main>
</body>
</html>
```